Kelvane Plumbing Business cards

Company is Kelvane Plumbing.
name Dashel Morrowby, I am a plumber, drainer, gasfitter and roofer
Mobile: 0431 906 154
Email address: info@kelvaneplumbing.example (check out my website for some ideas)
Website: www.kelvaneplumbing.example
ABN: 82 916 203 471
LIC: 604517K

I am reliable all round plumber. I am a 24 hour emergency service. Kelvane Plumbing is a professional plumbing service in the Illawarra, South Coast, Southern Sydney and Southern Highland regions of NSW. We offer a 24 hour emergency service for piece of mind to our customers. Call us now to see how we can help you. Kelvane Plumbing approaches every job with attention to detail and excellent customer service. With our superior workmanship you can be confident that the job will be done right the first time around. You can rest assured with results that are guaranteed to last.

Target Market(s)

the general public

Contact Information for Business Card

look up website for some ideas something with similar colours to logo and new modern and to catch the eye.

Colors
fdfdfd
ffffff
000000
7f7f7f
aaaaaa
33a6d7
0492cd

Requirements
Must have
• all contact details
• company- Kelvane Plumbing
• name- Dashel Morrowby
• number mobile- 0431 906 154
• Email address- info@kelvaneplumbing.example
• Website- www.kelvaneplumbing.example
• ABN- 82 916 203 471
• LIC- 604517K

```html
<!DOCTYPE html>
<html lang="en">
<head>
<meta charset="utf-8">
<title>Kelvane Plumbing Business Cards</title>
<link rel="stylesheet" href="https://fonts.googleapis.com/css2?family=Open+Sans:wght@400;700&family=PT+Sans+Narrow&display=swap">
<style>
  :root {
    --backdrop: #3d3d3d;
    --card: #141414;
    --blue: #219fcd;
    --blue-deep: #0492cd;
    --white: #ffffff;
    --off-white: #e9e9e9;
    --grey: #7f7f7f;
  }
  * { margin: 0; padding: 0; box-sizing: border-box; }
  html, body { width: 1200px; height: 1200px; overflow: hidden; }
  body { background: var(--backdrop); position: relative; font-family: "Open Sans", sans-serif; color: var(--white); }

  .card { position: absolute; background: var(--card); overflow: hidden; }

  .card-front { left: 282px; top: 176px; width: 632px; height: 360px; }
  .front-name {
    position: absolute; left: 0; right: 0; top: 128px; text-align: center;
    font-weight: 700; font-size: 40px; color: var(--blue); letter-spacing: 1px;
  }
  .front-band {
    position: absolute; left: 0; top: 296px; width: 100%; height: 35px; background: var(--blue);
    font-family: "PT Sans Narrow", sans-serif; font-size: 22px; line-height: 35px;
  }
  .front-band .abn { position: absolute; left: 136px; }
  .front-band .lic { position: absolute; left: 376px; }

  .card-back { left: 287px; top: 642px; width: 627px; height: 358px; }
  .back-brand {
    position: absolute; left: 40px; top: 110px; width: 280px; height: 80px;
    display: flex; align-items: center; justify-content: center; gap: 12px;
  }
  .brand-dot { width: 22px; height: 22px; border-radius: 50%; background: var(--blue); flex: none; }
  .brand-name { font-weight: 700; font-size: 24px; line-height: 1.15; color: var(--blue); }
  .divider { position: absolute; left: 323px; top: 86px; width: 2px; height: 148px; background: var(--white); }
  .holder-name { position: absolute; left: 351px; top: 80px; font-weight: 700; font-size: 25px; }
  .contact-list { position: absolute; left: 350px; top: 127px; list-style: none; }
  .contact-list li { display: flex; align-items: center; height: 31px; font-size: 19.5px; font-family: "PT Sans Narrow", sans-serif; }
  .contact-list svg { width: 22px; height: 22px; margin-right: 13px; flex: none; }

  .decor-area {
    position: absolute; left: 0; bottom: 0; width: 100%; height: 100px;
    background: linear-gradient(to bottom right, var(--card) 0%, #3a3a3a 45%, var(--blue) 100%);
  }
</style>
</head>
<body>
  <section class="card card-front">
    <div class="front-name">Kelvane Plumbing</div>
    <div class="front-band">
      <span class="abn">ABN- 82 916 203 471</span>
      <span class="lic">LIC- 604517K</span>
    </div>
  </section>

  <section class="card card-back">
    <div class="back-brand">
      <span class="brand-dot"></span>
      <span class="brand-name">Kelvane<br>Plumbing</span>
    </div>
    <div class="divider"></div>
    <div class="holder-name">Dashel Morrowby</div>
    <ul class="contact-list">
      <li>
        <svg viewBox="0 0 22 22"><circle cx="11" cy="11" r="11" fill="#e9e9e9"/><path d="M7 5.5c1 0 2 2.4 2 3s-1 1-.8 1.6c.5 1.5 2 3 3.4 3.5.6.2 1-.8 1.6-.8s3 1 3 2-1.4 2-2.4 2C9.6 16.8 5.2 12.4 5 8c0-1 1-2.5 2-2.5z" fill="#141414"/></svg>
        0431 906 154
      </li>
      <li>
        <svg viewBox="0 0 22 22"><circle cx="11" cy="11" r="11" fill="#e9e9e9"/><rect x="5.5" y="7" width="11" height="8" rx="1" fill="#141414"/><path d="M5.8 7.5l5.2 4 5.2-4" stroke="#e9e9e9" stroke-width="1.2" fill="none"/></svg>
        info@kelvaneplumbing.example
      </li>
      <li>
        <svg viewBox="0 0 22 22"><circle cx="11" cy="11" r="11" fill="#e9e9e9"/><circle cx="11" cy="11" r="6" fill="none" stroke="#141414" stroke-width="1.4"/><path d="M5 11h12M11 5c-2.5 3-2.5 9 0 12M11 5c2.5 3 2.5 9 0 12" stroke="#141414" stroke-width="1.2" fill="none"/></svg>
        www.kelvaneplumbing.example
      </li>
    </ul>
    <div class="decor-area" role="img" aria-label="Decorative flowing wave band in white and blue"></div>
  </section>
</body>
</html>
```